We are looking to recreate our Harlow & Partners Jobsite Sign. This sign will be placed by the street at each of our jobsites. We want to keep this sign simple, but at the same time, want to add a catching appeal to the design for anyone passing by. We want to stick to a two color scheme (Harlow Blue, and White). Please only use the Company Logo that I have uploaded for this project. Please also see a mock up of what we would like to include on this sign. The Sign Dimensions will be 4' x 8'. Please keep all verbiage uniform with the verbiage on the sample design I have uploaded. LET YOUR CREATIVITY FLOW!

```html
<!DOCTYPE html>
<html lang="en">
<head>
<meta charset="utf-8">
<title>Harlow &amp; Partners Jobsite Sign</title>
<link rel="stylesheet" href="https://fonts.googleapis.com/css2?family=Noto+Serif:wght@700&display=swap">
<style>
  :root {
    --harlow-blue: #1f2590;
    --band-blue: #2a2f8c;
    --band-blue-deep: #1c228a;
    --sign-white: #ffffff;
    --backdrop: #8ec3f2;
  }
  * { margin: 0; padding: 0; box-sizing: border-box; }
  html, body {
    width: 1109px;
    height: 1200px;
    overflow: hidden;
    background: var(--backdrop);
    font-family: "Noto Serif", Georgia, serif;
    font-weight: 700;
  }
  .canvas {
    position: relative;
    width: 1109px;
    height: 1200px;
  }
  .jobsite-sign {
    position: absolute;
    left: 54px;
    top: 350px;
    width: 1000px;
    height: 500px;
    background: var(--sign-white);
    box-shadow: 0 3px 10px rgba(0, 0, 0, 0.25);
    overflow: hidden;
  }
  .sign-header {
    position: absolute;
    top: 28px;
    left: 0;
    width: 100%;
    display: flex;
    justify-content: center;
    align-items: center;
    color: var(--harlow-blue);
  }
  .company-name {
    text-align: right;
    line-height: 1;
    padding-right: 26px;
  }
  .company-name__main {
    display: block;
    font-size: 66px;
    letter-spacing: -1px;
  }
  .company-name__sub {
    display: block;
    font-size: 32px;
    margin-top: 4px;
  }
  .header-divider {
    width: 3px;
    height: 110px;
    background: var(--harlow-blue);
  }
  .trade-title {
    padding-left: 28px;
    text-align: center;
    font-size: 46px;
    line-height: 1.05;
  }
  .info-band {
    position: absolute;
    left: 0;
    top: 162px;
    width: 958px;
    height: 228px;
    background: linear-gradient(90deg, var(--band-blue), var(--band-blue-deep));
    border-radius: 0 114px 114px 0;
    color: var(--sign-white);
    text-align: center;
    padding-right: 40px;
  }
  .tagline {
    font-size: 46px;
    margin-top: 22px;
    line-height: 1.2;
  }
  .location-license {
    font-size: 30px;
    letter-spacing: 1px;
    margin-top: 10px;
  }
  .website {
    font-size: 52px;
    letter-spacing: 1px;
    margin-top: 4px;
  }
  .sign-footer {
    position: absolute;
    left: 44px;
    right: 44px;
    top: 405px;
    height: 80px;
    display: flex;
    justify-content: space-between;
    align-items: center;
    color: var(--harlow-blue);
  }
  .phone {
    font-size: 64px;
    letter-spacing: 1px;
  }
  .social-links {
    display: flex;
    gap: 22px;
  }
  .social-dot {
    width: 56px;
    height: 56px;
    border-radius: 50%;
    background: var(--harlow-blue);
  }
</style>
</head>
<body>
<main class="canvas">
  <section class="jobsite-sign">
    <header class="sign-header">
      <div class="company-name">
        <span class="company-name__main">Harlow</span>
        <span class="company-name__sub">&amp; Partners, Inc.</span>
      </div>
      <div class="header-divider"></div>
      <div class="trade-title">General<br>Contractors</div>
    </header>

    <div class="info-band">
      <p class="tagline">“We Build Lasting Confidence”</p>
      <p class="location-license">Lakemont, Florida - CGC1598214</p>
      <p class="website">harlowpartners.net</p>
    </div>

    <footer class="sign-footer">
      <p class="phone">Call: 407-555-0142</p>
      <div class="social-links" aria-label="Social media links">
        <span class="social-dot"></span>
        <span class="social-dot"></span>
        <span class="social-dot"></span>
      </div>
    </footer>
  </section>
</main>
</body>
</html>
```